Vostrel Holdings Web Design

Vostrel Holdings Limited Shenzhen

This project is a 10 page launch website.
Our client is seeking a contemporary homepage design for a Holdings company. Once we are happy with the homepage design and select designer we will request a secondary page design.

Please see attached company LOGO for an idea of style, it incorporates the traditional Chinese furniture lattice work. The Quillmoor website is one of our clients favorite so we would like to see a similar homepage design to this website.

Use the websites below for reference purpose. The first two are Chinese and the second two are international. We would like to see elements of both but more focus on international design.

http://www.evergrande.com/http://www.brevandgroup.com/pub/default.aspx http://www.quillmoor.com/zh/maldives_resortone/
http://www.vellune-studio.com
http://media-cache-ec0.fotrelix.com/originals/41/a3/90/41a390c1f5b7d2e8a6c4f0b9e3d71a55.jpg

Company Background
VOSTREL HOLDINGS, located in Qianhai, China, is a new real-estate project operator, structuring urban-rural real-estate investment and development, and industrial fund investment. The company also invests in supply chain management and supporting infrastructures. To create new spaces and livable cities Vostrel Holdings develop win-win strategic partnerships with a number of institutions. Currently cooperating with Harrow East Lindcombe, China urban and rural integrated demonstration.

Target Market(s)

B2B property investment. Target market customers are senior level management/decision makers of large corporations. Focusing geographically on the domestic market first and expanding internationally in 2nd and 3rd years.

Industry/Entity Type

Investment

Requirements
Must have
• Since this is a new company, we would like to the website representing growth and power, E.g. like a growing tree.
Should not have
• Low-level vectors such as curency symbols, American dollar.

```html
<!DOCTYPE html>
<html lang="en">
<head>
<meta charset="utf-8">
<title>Vostrel Holdings</title>
<link href="https://fonts.googleapis.com/css2?family=Roboto:wght@300;400;500;700&family=Rock+Salt&display=swap" rel="stylesheet">
<style>
:root{
  --purple:#8d5a92;
  --purple-light:#a572a9;
  --purple-deep:#6d3f74;
  --hero-top:#5a3562;
  --hero-mid:#8a5c90;
  --nav-dark:#2c2a2d;
  --nav-light:#4a474b;
  --footer-dark:#2a2a2a;
  --ink:#333333;
  --ink-soft:#555555;
  --white:#ffffff;
}
*{margin:0;padding:0;box-sizing:border-box}
html,body{width:1200px;height:2343px;overflow:hidden}
body{position:relative;font-family:"Roboto",Arial,sans-serif;color:var(--ink);background:var(--white)}
.abs{position:absolute}

/* hero */
.hero{position:absolute;left:0;top:0;width:1200px;height:668px;
  background:radial-gradient(ellipse 500px 220px at 600px 60px,#e4c6e7 0%,rgba(200,160,205,.6) 35%,rgba(0,0,0,0) 75%),
  linear-gradient(180deg,var(--hero-top) 0%,var(--hero-mid) 45%,#9c7aa1 75%,#8c6a92 100%);}
.hero-shadow{position:absolute;left:0;top:664px;width:1200px;height:8px;background:linear-gradient(180deg,#3b2340,rgba(0,0,0,0))}
.brand{position:absolute;left:400px;top:96px;width:400px;text-align:center;font-family:"Roboto",Arial,sans-serif;font-weight:400;font-size:20px;color:var(--white);letter-spacing:.5px}
.lang{position:absolute;left:1003px;top:20px;width:82px;height:25px;background:linear-gradient(#8a6a8f,#5d4263);border-radius:3px;color:#fff;font-size:12px;padding:5px 9px}
.lang svg{position:absolute;right:8px;top:10px}
.scribble{font-family:"Rock Salt",cursive;color:#fff;font-size:14px;white-space:nowrap}
.hire{left:1018px;top:62px;transform:rotate(-25deg)}
.nav{position:absolute;left:115px;top:151px;width:970px;height:45px;background:linear-gradient(var(--nav-light),var(--nav-dark));display:flex;border-radius:2px;box-shadow:0 2px 4px rgba(0,0,0,.4)}
.nav a{color:#fff;text-decoration:none;font-size:12.5px;font-weight:500;white-space:nowrap;display:flex;align-items:center;padding:0 10px;border-right:1px solid #1c1b1d;flex:1 1 auto;justify-content:center}
.nav a.active{background:linear-gradient(#b288b6,#7c4f84)}
.hero-title{position:absolute;left:0;width:1200px;top:252px;text-align:center;color:#fff;font-weight:300;font-size:58px}
.team{position:absolute;top:334px;left:367px;display:flex;gap:20px}
.team span{width:100px;height:100px;border-radius:50%;border:3px solid #fff;background:radial-gradient(circle at 50% 40%,#d9c2b4,#3c3a4a)}
.hero-text{position:absolute;left:170px;width:860px;top:446px;text-align:center;color:#fff;font-size:20px;line-height:27px}
.cta{position:absolute;left:542px;top:518px;width:106px;height:38px;border-radius:4px;background:linear-gradient(#b48ab8,#7d4f85);color:#fff;font-weight:700;font-size:16px;display:flex;align-items:center;justify-content:center;box-shadow:0 2px 4px rgba(0,0,0,.35)}
.know{left:672px;top:555px;transform:rotate(-6deg)}
.dots{position:absolute;top:626px;left:563px;display:flex;gap:6px}
.dots i{width:14px;height:14px;border-radius:50%;background:#ddd}
.dots i.on{background:var(--purple-light);border:2px solid #ddd}

/* welcome */
.welcome{position:absolute;left:0;top:672px;width:1200px;height:378px;background:linear-gradient(180deg,#8c5a92,#9a6ba0)}
.welcome h2{position:absolute;width:1200px;top:62px;text-align:center;color:#fff;font-weight:300;font-size:28px}
.welcome h1{position:absolute;width:1200px;top:92px;text-align:center;color:#fff;font-weight:300;font-size:48px}
.welcome p{position:absolute;left:150px;width:900px;text-align:center;color:#fff;font-size:13px;line-height:18px}

/* gallery */
.gallery{position:absolute;left:0;top:1054px;width:1200px;height:597px;display:grid;grid-template-columns:repeat(4,1fr);grid-template-rows:repeat(3,1fr);gap:3px;background:#fff}
.gallery div{position:relative}
.g1{background:linear-gradient(160deg,#c9b48c,#7a6a54)}
.g2{background:linear-gradient(180deg,#3d4a86,#8a93b8 70%,#2a2a35)}
.g3{background:linear-gradient(180deg,#4a4a4a,#1f1f1f)}
.g4{background:linear-gradient(150deg,#a89478,#5e4e3e)}
.g5{background:linear-gradient(180deg,#7c5a48,#e07a3a 60%,#1e1510)}
.g6{background:linear-gradient(160deg,#9fb2c8,#8a7456)}
.g7{background:linear-gradient(180deg,#3d6fc2,#9bb5d8 55%,#5a4a3e)}
.g8{background:linear-gradient(150deg,#d4cbbd,#7e6c58)}
.g9{background:linear-gradient(180deg,#4f8ad8,#a8c4e4 60%,#6a7a8a)}
.g10{background:linear-gradient(160deg,#78a4d8,#d8c8b0)}
.g11{background:linear-gradient(180deg,#bfc8d2,#8a7a62 55%,#6a5a46)}
.g12{background:linear-gradient(160deg,#b8b4ac,#5a5046)}
.tile-overlay{position:absolute;inset:0;background:rgba(30,30,30,.82);color:#fff;text-align:center}
.tile-overlay h3{font-weight:400;font-size:24px;margin-top:32px}
.tile-icons{display:flex;justify-content:center;gap:6px;margin-top:14px}
.tile-icons span{width:32px;height:32px;background:#fff;display:flex;align-items:center;justify-content:center}
.tile-overlay p{font-size:13px;font-weight:700;line-height:16px;margin-top:16px;padding:0 12px}

/* news & services */
.section-title{position:absolute;color:var(--purple);font-weight:300;font-size:36px}
.news{position:absolute;left:115px;top:1783px;width:600px;list-style:none}
.news li{position:relative;padding-left:30px;font-size:14px;line-height:17px;color:var(--ink);height:49px}
.news svg{position:absolute;left:0;top:2px}
.divider-v{position:absolute;left:764px;top:1719px;width:1px;height:312px;background:#dcdcdc}
.services{position:absolute;left:818px;top:1784px;list-style:none}
.services li{display:flex;align-items:center;gap:8px;font-size:14px;color:var(--ink);height:26.6px}
.services b{width:18px;height:18px;border-radius:50%;background:var(--purple);color:#fff;font-size:10px;font-weight:500;display:flex;align-items:center;justify-content:center}
.services li:first-child b{background:#222}

/* contact band */
.band{position:absolute;left:0;top:2069px;width:1200px;height:192px;background:var(--purple)}
.tweet{position:absolute;top:32px;width:1200px;text-align:center;color:#fff;font-size:11.5px}
.tweet strong{font-size:14px}
.tweet .dot{display:inline-block;width:18px;height:18px;border-radius:50%;background:#fff;vertical-align:-4px;margin-right:6px}
.band hr{position:absolute;left:115px;top:68px;width:970px;border:0;border-top:1px solid #b48cb8}
.contact{position:absolute;top:110px;display:flex;align-items:center;gap:14px;color:#fff;font-size:19px}
.contact .ic{width:36px;height:36px;border-radius:50%;background:#111;display:flex;align-items:center;justify-content:center}
.contact.phone{font-size:24px}

/* footer */
.footer{position:absolute;left:0;top:2261px;width:1200px;height:82px;background:var(--footer-dark)}
.footer nav{position:absolute;left:115px;top:30px;display:flex;gap:22px}
.footer nav a{color:#fff;font-size:11px;font-weight:500;text-decoration:none;white-space:nowrap}
.footer nav a.active{color:var(--purple-light)}
.copy{position:absolute;left:115px;top:53px;font-size:8px;color:#888}
.stay{left:891px;top:28px;font-size:13px}
.social{position:absolute;left:991px;top:25px;display:flex;gap:6px}
.social i{width:28px;height:28px;border-radius:50%;background:var(--purple-light)}
.social i:first-child{background:#fff}
</style>
</head>
<body>

<header class="hero" role="img" aria-label="Blurred purple-toned city skyline at dusk">
</header>
<div class="hero-shadow"></div>

<div class="brand">Vostrel Holdings</div>

<div class="lang">English
  <svg width="9" height="6" viewBox="0 0 9 6"><path d="M0 0h9L4.5 6z" fill="#fff"/></svg>
</div>
<div class="abs scribble hire">Hire Us</div>
<svg class="abs" style="left:1020px;top:80px" width="40" height="72" viewBox="0 0 40 72">
  <path d="M30 2 C10 20 8 40 12 64" stroke="#fff" stroke-width="2" fill="none"/>
  <path d="M4 56 L12 66 L19 55" stroke="#fff" stroke-width="2" fill="none"/>
</svg>

<nav class="nav">
  <a class="active" href="#">Home</a><a href="#">About Us</a><a href="#">Incorporate</a><a href="#">Trademarks</a><a href="#">Partners</a><a href="#">Services</a><a href="#">Registered Office</a><a href="#">Special Structures</a><a href="#">Blog</a><a href="#" style="border-right:0">Contact Us</a>
</nav>

<h1 class="hero-title">Lorem ipsum dolor sit amet</h1>
<div class="team">
  <span role="img" aria-label="Portrait of team member"></span>
  <span role="img" aria-label="Portrait of team member"></span>
  <span role="img" aria-label="Portrait of team member"></span>
  <span role="img" aria-label="Portrait of team member"></span>
</div>
<p class="hero-text">Lorem ipsum dolor sit amet, consectetur adipiscing elit. Nulla lobortis consequat mauris, eget eleifend nunc viverra viverra. Ut ac risus odio. Aliquam pretium purus sed nulla</p>
<div class="cta">Click Here</div>
<svg class="abs" style="left:626px;top:548px" width="48" height="40" viewBox="0 0 48 40">
  <path d="M46 30 C30 36 14 30 6 8" stroke="#fff" stroke-width="2" fill="none"/>
  <path d="M1 16 L5 6 L14 12" stroke="#fff" stroke-width="2" fill="none"/>
</svg>
<div class="abs scribble know">Know More</div>
<div class="dots"><i class="on"></i><i></i><i></i><i></i></div>

<section class="welcome">
  <h2>Welcome to</h2>
  <h1>Vostrel Holdings</h1>
  <p style="top:168px">Lorem ipsum dolor sit amet, consectetur adipiscing elit. Nulla lobortis consequat mauris, eget eleifend nunc viverra viverra. Ut ac risus odio. Aliquam pretium purus sed nulla feugiat blandit. Cras vel libero ut lacus eleifend tempor.</p>
  <p style="top:226px">Phasellus eleifend, magna non tincidunt accumsan, justo arcu cursus ipsum, non porttitor sapien quam vel magna. Maecenas elit nisl, molestie nec dapibus nec, aliquet a erat. Donec scelerisque lacus a libero suscipit auctor volutpat enim euismod. Mauris porta, lacus ut ullamcorper sodales, mauris tortor feugiat purus, nec aliquam neque purus ac metus. Nunc eleifend leo quis nisl hendrerit ultrices. Suspendisse quis feugiat elit. Fusce vitae dolor ac est tincidunt feugiat. Phasellus volutpat dui in sapien malesuada tempus placerat justo ultricies. Duis mollis ornare risus, ut consectetur mi tincidunt sit amet. Maecenas quis nibh ac orci tempus scelerisque ac et massa.</p>
</section>

<section class="gallery">
  <div class="g1" role="img" aria-label="Team reviewing plans on a building site"></div>
  <div class="g2" role="img" aria-label="Silhouetted workers under construction cranes"></div>
  <div class="g3" role="img" aria-label="Engineers in hard hats on site">
    <div class="tile-overlay">
      <h3>Mauris Tortor</h3>
      <div class="tile-icons">
        <span><svg width="16" height="16" viewBox="0 0 16 16"><path d="M6 10 L10 6 M4 8 L2 10 a2.8 2.8 0 0 0 4 4 L8 12 M12 8 L14 6 a2.8 2.8 0 0 0 -4 -4 L8 4" stroke="#222" stroke-width="2" fill="none"/></svg></span>
        <span><svg width="16" height="16" viewBox="0 0 16 16"><circle cx="6.5" cy="6.5" r="4.5" stroke="#222" stroke-width="2" fill="none"/><path d="M10 10 L15 15" stroke="#222" stroke-width="2.5"/></svg></span>
      </div>
      <p>Mauris porta, lacus ut ullamcorper sodales, mauris tortor feugiat purus, nec</p>
    </div>
  </div>
  <div class="g4" role="img" aria-label="Workers on timber scaffolding"></div>
  <div class="g5" role="img" aria-label="Excavator silhouetted against sunset"></div>
  <div class="g6" role="img" aria-label="Engineers discussing house construction"></div>
  <div class="g7" role="img" aria-label="Tower cranes over a building frame"></div>
  <div class="g8" role="img" aria-label="Site managers pointing at a structure"></div>
  <div class="g9" role="img" aria-label="Glass office towers with cranes"></div>
  <div class="g10" role="img" aria-label="Handshake with hard hat"></div>
  <div class="g11" role="img" aria-label="Excavator on a city construction site"></div>
  <div class="g12" role="img" aria-label="Engineers reading plans beside a building"></div>
</section>

<h2 class="section-title" style="left:115px;top:1720px">Latest News</h2>
<ul class="news">
  <li><svg width="16" height="17" viewBox="0 0 16 17"><rect x="0" y="2" width="16" height="15" fill="var(--purple)"/><rect x="2" y="6" width="12" height="9" fill="#fff"/><path d="M4 0v4M12 0v4" stroke="var(--purple)" stroke-width="2"/></svg>Lorem ipsum dolor sit amet, consectetur adipiscing elit. Nulla lobortis consequat mauris, eget eleifend nunc viverra viverra. Ut ac risus odio....</li>
  <li><svg width="16" height="17" viewBox="0 0 16 17"><rect x="0" y="2" width="16" height="15" fill="var(--purple)"/><rect x="2" y="6" width="12" height="9" fill="#fff"/><path d="M4 0v4M12 0v4" stroke="var(--purple)" stroke-width="2"/></svg>Aliquam pretium purus sed nulla feugiat blandit. Cras vel libero ut lacus eleifend tempor. Phasellus eleifend, magna non tincidunt accumsan...</li>
  <li><svg width="16" height="17" viewBox="0 0 16 17"><rect x="0" y="2" width="16" height="15" fill="var(--purple)"/><rect x="2" y="6" width="12" height="9" fill="#fff"/><path d="M4 0v4M12 0v4" stroke="var(--purple)" stroke-width="2"/></svg>Lorem ipsum dolor sit amet, consectetur adipiscing elit. Nulla lobortis consequat mauris, eget eleifend nunc viverra viverra. Ut ac risus odio....</li>
  <li><svg width="16" height="17" viewBox="0 0 16 17"><rect x="0" y="2" width="16" height="15" fill="var(--purple)"/><rect x="2" y="6" width="12" height="9" fill="#fff"/><path d="M4 0v4M12 0v4" stroke="var(--purple)" stroke-width="2"/></svg>Aliquam pretium purus sed nulla feugiat blandit. Cras vel libero ut lacus eleifend tempor. Phasellus eleifend, magna non tincidunt accumsan...</li>
  <li><svg width="16" height="17" viewBox="0 0 16 17"><rect x="0" y="2" width="16" height="15" fill="var(--purple)"/><rect x="2" y="6" width="12" height="9" fill="#fff"/><path d="M4 0v4M12 0v4" stroke="var(--purple)" stroke-width="2"/></svg>Lorem ipsum dolor sit amet, consectetur adipiscing elit. Nulla lobortis consequat mauris, eget eleifend nunc viverra viverra. Ut ac risus odio....</li>
</ul>

<div class="divider-v"></div>

<h2 class="section-title" style="left:818px;top:1720px">Our Services</h2>
<ol class="services">
  <li><b>1</b>Lorem ipsum dolor sit amet,</li>
  <li><b>2</b>Consectetur adipiscing elit. Nulla</li>
  <li><b>3</b>Lobortis consequat mauris, eget</li>
  <li><b>4</b>Eleifend nunc viverra viverra. Ut ac</li>
  <li><b>5</b>Risus odioAliquam pretium purus</li>
  <li><b>6</b>Sed nulla feugiat blandit. Cras vel</li>
  <li><b>7</b>Libero ut lacus eleifend tempor.</li>
  <li><b>8</b>Phasellus eleifend, magna non</li>
  <li><b>9</b>Tincidunt accumsan</li>
</ol>

<section class="band">
  <p class="tweet"><span class="dot"></span><strong>@Lorem ipsum</strong> dolor sit amet, consectetur adipiscing elit. Nulla lobortis consequat mauris, eget eleifend nunc viverra viverra. <strong><em>http://acrisusodio.com</em></strong></p>
  <hr>
  <div class="contact phone" style="left:133px">
    <span class="ic"><svg width="18" height="18" viewBox="0 0 18 18"><path d="M4 1 L7 5 L5 7 C6 10 8 12 11 13 L13 11 L17 14 L15 17 C8 17 1 10 1 3 Z" fill="#fff"/></svg></span>0000 0000 000
  </div>
  <div class="contact" style="left:430px">
    <span class="ic"><svg width="18" height="13" viewBox="0 0 18 13"><rect width="18" height="13" rx="1" fill="#fff"/><path d="M1 1 L9 7 L17 1" stroke="#111" stroke-width="1.5" fill="none"/></svg></span>support@vostrelholdings.com
  </div>
  <div class="contact" style="left:785px">
    <span class="ic"><svg width="20" height="16" viewBox="0 0 20 16"><path d="M1 6 C5 1 15 1 19 6 L16 8 L14 5 C11 4 9 4 6 5 L4 8 Z" fill="#fff"/><rect x="5" y="9" width="10" height="6" rx="1" fill="#fff"/></svg></span>support@vostrelholdings.com
  </div>
</section>

<footer class="footer">
  <nav>
    <a class="active" href="#">Home</a><a href="#">About Us</a><a href="#">Incorporate</a><a href="#">Trademarks</a><a href="#">Partners</a><a href="#">Services</a><a href="#">Registered Office</a><a href="#">Special Structures</a><a href="#">Blog</a><a href="#">Contact Us</a>
  </nav>
  <p class="copy">COPYRIGHT © 2013 Vostrel Holdings Limited.&nbsp; TERMS OF USE | PRIVACY POLICY</p>
  <div class="abs scribble stay">Stay with us</div>
  <div class="social"><i></i><i></i><i></i></div>
</footer>

</body>
</html>
```